Interactive Children's Media Book Company Website Design

We need a website DESIGN (no coding required) for a new interactive children's media book company called Tovira Studios.

We develop high-quality interactive children's books for the Slate/Pocketphone that seeks to delight and inspire young and old alike. Our stories are filled with heart and spirit, and we seek to breathe magic back into books so that people fall back in love with reading.

Tovira means "butterfly" in Korean. It plays on the idea that a caterpillar metamorphoses into a butterfly - and in the same way, our readers are transformed through the journey of experiencing our interactive books.

We're looking for something based on the ATTACHED LOGO DESIGN for our company. A website that's professional, modern, fun and inviting; easy to read and not-cluttered, but still portraying the feeling of innocence and childhood.

We're looking for something that resonates the magical experience we want to create for our readers. Specific requirements on pages, tabs, content, etc are below.

Industry/Entity Type

It Company

Requirements
Nice to have
• There are 7 tabs on the Homepage of the website: HOME, GRANDPA, ABOUT US, CAREERS, NEWS, CONTACT US, SHOP. (But there is an extra page called THEIR GARDEN, which will be a sub-page under Grandpa).

HOME
• Would be great to have some key images of our book (3-4 screen shots) as the key focus of the homepage that automatically scroll through every few seconds. (Placeholder image attached). The images would link to the “Grandpa” page.
• Company logo (attached to brief) and slogan: “A new era of children’s media” quite prominent on page.
• Key text content to be on page: “Tovira means “butterfly” in Korean. Just as a caterpillar transforms into a butterfly, Tovira Studios takes the reader on an unforgettable journey of metamorphosis through our stories. We turn children’s books into a high-quality interactive experience on mobile platforms - breathing magic back into books, and inspiring people to fall back in love with reading. Through our unique characters full of heart and spirit, our stories delight and inspire young and old alike.”
• Chirper & Frendly Like & Frendly page link icons.
• Section on Latest News with a few of the latest entries.
• Section on latest sister images & comments that visitors have posted, which takes you to the “Their Garden” page.

GRANDPA
• The title for this page is “Grandpa Keeps a Secret Garden”
• There will be a little Slate/Pocketphone icon (placeholder attached) for this book.
• There will be a link to the App Store to buy the app book.
• Key text content on this page: “Our debut interactive media book is coming soon on the Slate and Pocketphone! “Grandpa Keeps a Secret Garden” touches on the beautiful and inextricable (albeit sometimes frustrating!) bond between sisters.”
• There will be a section on “Features” which lists all the various special features the app book includes.
• There will be a Cliptube clip embedded into the page, which shows how the app book works.
• A section that says: “Do you have a sister who’s not like other sisters? Share a photo and tell us about her!” which links to the sub-page “Their Garden”.
• Under this, there may be the most recent few images submitted by the public, which when clicked on, would also link to the sub-page “Their Garden”.

THEIR GARDEN
• The main text on the page: “Do you have a sister who’s not like other sisters? Share a photo and tell us about her!”
• Main body of the page is a gallery of all the photos that have been submitted. If you click on each of the images, you get the comments that people have submitted with the photos.
• The page would also have a Submit Comments Form, where people can upload a picture of their sister(s) and write a comment to accompany the image.

ABOUT US
• Introductory text on page: “It was a chance conversation at Harbourview Terminal, where two friends discovered they shared a dream to create quality children's media. Both of them were excited by the possibilities of using new digital platforms to inspire and educate a younger generation. From that idea Tovira Studios was born. We seek to be the chrysalis of story telling - to inspire the hearts and minds of our generation, and generations to come.”
• Section to “Join the Mailing List” where they can put their email address in and submit.
• Bios of 2x people with photos (bios in word doc attached) (do not have photos yet).

CAREERS
• The main text on the page: “We are always on the lookout for talented people to join our team. If you are a writer, illustrator, animator, iOS/android developer, musician, creative-writing translator - or have something special to offer Tovira Studios - we are keen to hear from you. Send us a message through the Contact Us tab above.”

NEWS
• Regular News page, with blog-type entries.

CONTACT US
• Online submit Contact Us form
• The main text on page: “Our studio is based in the Marram Arts Hub, 14 Pellham Street, Ardlow, Wellington. Marram is a professional, creative collective - with four separate studios, gallery, and retail store. For more information on Marram, visit: http://www.marramhub.example.nz”
• “We would love to hear from you! Whether you have questions, ideas, comments, or just want to say hullo - please leave us a message and we will get back to you soon.”
• Including image of the premises (Marram image attached to brief).

SHOP
• Where visitors can purchase merchandise (t-shirts, mugs, etc) of the book/company.

```html
<!DOCTYPE html>
<html lang="en">
<head>
<meta charset="utf-8">
<title>Tovira Studios – Grandpa Keeps a Secret Garden</title>
<link rel="stylesheet" href="https://fonts.googleapis.com/css2?family=Arimo:wght@400;700&family=Varela+Round&family=Mountains+of+Christmas:wght@400;700&display=swap">
<style>
:root{
  --lavender:#b6a3da;
  --lavender-soft:#e4dcf2;
  --lavender-pale:#f4f0fa;
  --purple:#7a4fc8;
  --purple-dark:#5b3aa6;
  --video:#5f4aa8;
  --heading-blue:#2a8fd0;
  --script-blue:#2f8fcf;
  --sky:#28b8ea;
  --sky-deep:#1f8fd8;
  --text:#4a4a4a;
  --link:#4a3a9a;
  --white:#ffffff;
  --line:#d6d0e2;
}
*{box-sizing:border-box;margin:0;padding:0}
html,body{width:814px;height:1200px;overflow:hidden}
body{position:relative;font-family:"Arimo",Arial,sans-serif;color:var(--text);
  background:linear-gradient(180deg,#ad98d6 0,#cdbfe7 200px,#e2daf1 300px,#f6f3fb 420px,#ffffff 520px,#ffffff 1090px,#e8e2f2 1110px,#f4f1f9 1160px,#c6b5e2 1200px)}
.glow{position:absolute;left:140px;top:-180px;width:560px;height:520px;border-radius:50%;
  background:radial-gradient(closest-side,rgba(255,255,255,.85),rgba(255,255,255,0))}
.abs{position:absolute}
.hero-band{left:0;top:300px;width:814px;height:84px;background:linear-gradient(180deg,#dcd1ee,#ece6f6);border-top:1px solid #efeaf8;border-bottom:1px solid #cfc3e6}

.brand{left:62px;top:28px;display:flex;align-items:center;gap:10px}
.brand-dot{width:40px;height:40px;border-radius:50%;background:var(--purple)}
.brand-name{font-family:"Varela Round",sans-serif;font-size:38px;color:var(--purple-dark);line-height:1}

.nav{left:262px;top:84px;display:flex;gap:4px}
.nav a{display:block;width:71px;height:29px;line-height:30px;text-align:center;text-decoration:none;
  font-family:"Varela Round",sans-serif;font-size:12px;color:var(--white);
  background:linear-gradient(180deg,#8f63d6,#6a42b8);border-radius:5px 5px 0 0}

.hero-card{left:66px;top:110px;width:672px;height:250px;background:var(--white);border-radius:6px;
  box-shadow:0 2px 8px rgba(90,60,150,.28)}
.hero-art{left:82px;top:132px;width:316px;height:209px;background:linear-gradient(160deg,#5fa05a,#b98a56 55%,#7a8ad0)}
.hero-panel{left:398px;top:132px;width:332px;height:209px;background:linear-gradient(120deg,var(--sky-deep),var(--sky) 70%,#55d0f2)}
.slogan{left:420px;top:190px;width:300px;text-align:center;font-family:"Mountains of Christmas",cursive;font-weight:700;
  font-size:34px;line-height:40px;color:var(--white)}
.dots{left:91px;top:318px;display:flex;gap:5px}
.dots span{width:14px;height:14px;border-radius:50%;border:2px solid var(--white);background:rgba(255,255,255,.35)}
.hero-btn{left:390px;top:322px;width:216px;height:35px;border-radius:5px;background:linear-gradient(180deg,#9d6fe0,#6d44bd);
  color:var(--white);font-weight:700;font-size:12px;text-align:center;line-height:35px}
.devices{left:618px;top:276px;width:120px;height:102px;border-radius:6px;background:linear-gradient(135deg,#3a3a44,#b86fc6 60%,#2c2c34)}

.social{left:34px;top:262px;display:flex;flex-direction:column;gap:3px}
.social span{width:33px;height:30px;background:var(--sky-deep);color:var(--white);font-size:7px;text-align:center;line-height:30px;border-radius:0 3px 3px 0}

.book-card{left:67px;top:400px;width:283px;height:428px;background:var(--white);border:1px solid #d9d3e6;border-radius:6px;
  box-shadow:0 2px 6px rgba(90,60,150,.15);padding:12px 12px 0 11px}
.book-card h2{font-weight:400;font-size:19px;line-height:28px;color:var(--heading-blue)}
.book-card p{font-size:9.5px;line-height:12px;margin-top:4px}
.book-card hr{border:0;border-top:1px solid var(--line);margin:12px 6px 10px}
.features{list-style:none;margin-top:7px}
.features li{font-size:9.5px;line-height:18.7px;padding-left:8px;position:relative}
.features li::before{content:"";position:absolute;left:0;top:7px;border-left:4px solid var(--heading-blue);border-top:3px solid transparent;border-bottom:3px solid transparent}

.btn{position:absolute;border-radius:4px;background:linear-gradient(180deg,#a273e2,#7146c2);color:var(--white);
  font-weight:700;font-size:12px;text-align:center;box-shadow:0 1px 3px rgba(60,30,120,.35)}
.book-title{left:374px;top:438px;width:182px;text-align:center;font-family:"Mountains of Christmas",cursive;font-size:24px;line-height:30px;color:var(--script-blue)}
.app-icon{left:622px;top:406px;width:69px;height:69px;border-radius:10px;background:linear-gradient(135deg,#f3a64c,#8cc36b);border:2px solid #ccc}
.store-badge{left:590px;top:484px;width:136px;height:32px;border-radius:16px;border:1px solid #aaa;background:linear-gradient(180deg,#fff,#e4e4e4);
  display:flex;align-items:center;gap:6px;padding-left:12px}
.store-badge i{width:14px;height:20px;border-radius:2px;background:linear-gradient(135deg,#333,#b86fc6)}
.store-badge b{font-weight:400;font-size:11px;color:#333;line-height:11px}
.store-badge small{display:block;font-size:8px;color:#555}
.version{left:602px;top:532px;width:120px;text-align:center;font-size:12px;line-height:15px;color:#444}
.rule{height:1px;background:linear-gradient(90deg,rgba(200,190,220,0),#cdc4dd 20%,#cdc4dd 80%,rgba(200,190,220,0))}

.video{left:386px;top:612px;width:338px;height:194px;background:var(--video)}
.video-mark{left:645px;top:760px;font-size:12px;font-weight:700;color:#3c2c7a}
.video-bar{left:386px;top:790px;width:338px;height:16px;background:#1e1e1e;color:#bbb;font-size:6px;line-height:16px}

.share h2{font-weight:400;font-size:19px;line-height:22px;color:var(--heading-blue)}
.share p{font-size:9.5px;line-height:12px;margin-top:6px}
.gallery{left:418px;top:876px;width:276px;height:148px;border:1px solid #cfc8dd;border-radius:4px;background:var(--white);box-shadow:0 1px 4px rgba(90,60,150,.2)}
.gallery-slide{left:426px;top:883px;width:261px;height:134px;background:var(--video);border-radius:3px}
.gallery-dots{left:434px;top:998px;display:flex;gap:3px}
.gallery-dots span{width:11px;height:11px;border-radius:50%;border:1.5px solid var(--white);background:rgba(255,255,255,.4)}
.caption{left:418px;top:1030px;width:276px;text-align:center;font-size:9.5px;color:#555}

.footer-band{left:0;top:1110px;width:814px;height:54px;border-top:1px solid #e2dbee;border-bottom:1px solid #d8cfe9}
.copyright{left:68px;top:1130px;font-size:9.5px;color:var(--link)}
.footer-links{right:68px;top:1130px;font-size:9.5px;color:var(--link)}
</style>
</head>
<body>
<div class="glow"></div>
<div class="abs hero-band"></div>

<header>
  <div class="abs brand"><span class="brand-dot"></span><span class="brand-name">Tovira</span></div>
  <nav class="abs nav">
    <a href="#">Home</a><a href="#">About Us</a><a href="#">Grandpa</a><a href="#">Shop</a><a href="#">Careers</a><a href="#">Contact Us</a>
  </nav>
</header>

<section>
  <div class="abs hero-card"></div>
  <div class="abs hero-art" role="img" aria-label="Illustrated scene from the book with its young heroine in a garden"></div>
  <div class="abs hero-panel"></div>
  <div class="abs slogan">A new era of<br>children’s media</div>
  <div class="abs dots"><span></span><span></span><span></span><span></span></div>
  <div class="abs hero-btn">Available on Pocketphone &amp; Slate</div>
  <div class="abs devices" role="img" aria-label="Phone and tablet showing the app"></div>
  <div class="abs social"><span>Frendly</span><span>Chirper</span></div>
</section>

<section class="abs book-card">
  <h2>Grandpa Keeps a Secret<br>Garden</h2>
  <p>Our debut interactive media book is coming soon on the Slate and Pocketphone! “Grandpa Keeps a Secret Garden” touches on the beautiful and inextricable (albeit sometimes frustrating!) bond between sisters.</p>
  <hr>
  <h2>Features</h2>
  <p>Lorem ipsum dolor sit amet, consectetur adipiscing elit. Fusce ut turpis tellus. Nulla eu elit quam. Vivamus convallis tincidunt nibh quis auctor. Aliquam in sem nisl, interdum aliquet felis.</p>
  <ul class="features">
    <li>Lorem ipsum</li><li>Dolor sit amet</li><li>Consectetur adipiscing</li><li>Fusce ut turpis tellus</li><li>Nulla eu elit quam</li><li>Fusce ut turpis tellus</li><li>Nulla eu elit quam</li>
  </ul>
</section>
<div class="btn" style="left:100px;top:774px;width:216px;height:36px;line-height:36px">Download App from Appstall</div>

<div class="abs book-title">“Grandpa Keeps a Secret Garden”</div>
<div class="btn" style="left:396px;top:521px;width:138px;height:26px;line-height:26px">Their Garden</div>
<div class="abs app-icon" role="img" aria-label="App icon for the book"></div>
<div class="abs store-badge"><i></i><b>Available App<small>For Pocketphone &amp; Slate</small></b></div>
<div class="abs version">Version 1.1<br>Coming Soon</div>
<div class="abs rule" style="left:396px;top:586px;width:324px"></div>

<div class="abs video"></div>
<svg class="abs" style="left:540px;top:684px" width="36" height="36" viewBox="0 0 36 36"><path d="M4 2 L32 18 L4 34 Z" fill="#fff"/></svg>
<div class="abs video-mark">Cliptube</div>
<div class="abs video-bar">
  <svg class="abs" style="left:6px;top:4px" width="8" height="8" viewBox="0 0 8 8"><path d="M0 0 L8 4 L0 8Z" fill="#fff"/></svg>
  <span class="abs" style="left:44px">0:00 / 6:50</span>
  <span class="abs" style="left:86px;top:7px;width:215px;height:2px;background:#555"></span>
  <span class="abs" style="left:318px;top:4px;width:12px;height:8px;background:#ddd;border-radius:1px"></span>
</div>

<div class="abs rule" style="left:66px;top:852px;width:666px"></div>

<section class="abs share" style="left:78px;top:872px;width:262px">
  <h2>Do you have a sister who’s not<br>like other sisters?</h2>
  <p>Lorem ipsum dolor sit amet, consectetur adipiscing elit. Fusce ut turpis tellus. Nulla eu elit quam. Lorem ipsum dolor sit amet, consectetur adipiscing elit. Fusce ut turpis tellus. Nulla eu elit quam.</p>
  <p>Lorem ipsum dolor sit amet, consectetur adipiscing elit. Fusce ut turpis tellus. Nulla eu elit quam.</p>
</section>
<div class="btn" style="left:78px;top:1009px;width:216px;height:35px;line-height:35px">Share a photo and tell us about her!</div>
<div class="abs" style="left:356px;top:864px;width:1px;height:180px;background:var(--line)"></div>

<div class="abs gallery"></div>
<div class="abs gallery-slide" role="img" aria-label="Photo submitted by a reader"></div>
<div class="abs gallery-dots"><span></span><span></span><span></span><span></span></div>
<div class="abs caption">Lorem ipsum dolor sit amet, consectetur adipiscing elit.</div>
<svg class="abs" style="left:376px;top:936px" width="32" height="32" viewBox="0 0 32 32"><circle cx="16" cy="16" r="15" fill="#f2f0f6" stroke="#cfc8dd"/><path d="M21 16 H11 M15 11 L10 16 L15 21" stroke="#4a3aa0" stroke-width="3" fill="none"/></svg>
<svg class="abs" style="left:702px;top:936px" width="32" height="32" viewBox="0 0 32 32"><circle cx="16" cy="16" r="15" fill="#f2f0f6" stroke="#cfc8dd"/><path d="M11 16 H21 M17 11 L22 16 L17 21" stroke="#4a3aa0" stroke-width="3" fill="none"/></svg>

<footer>
  <div class="abs footer-band"></div>
  <div class="abs copyright">© Copyright 2011 Tovira Studios</div>
  <div class="abs footer-links">Privacy | Sitemap | Contact</div>
</footer>
</body>
</html>
```